Learning Horizon Collective Website

Background

Learning Horizon Collective (LHC) is a newly established consultancy that focuses on education, primarily improving schools and universities. The company is registered in Dubai.

Domain name is learnhorizonco.com, the logo for LHC is attached as is the registered business address

Scope

LHC requests designers to design and build a website that initially includes the following key pages/sections.

• About us/our story
• Our people
• Our services
• Our work
• Contact us/social media

Some examples of websites that are similar to the look and feel of a new contemporary startup like LHC include the following:
http://www.telvano.co/journal/
https://www.quorimadvisory.com/

Content to be provided by LHC. In addition, LHC wishes the successful designer to set up all email and social media accounts required.

Target Market(s)

Government Education departments, donors, Private school chains, school owners, NGOs, investors

Industry/Entity Type

Education

Number of Pages Required

3 page

Font styles to use
Sans Serif

Colors

Designer to choose colors to be used in the design.

Requirements
Must have
• • About us/our story
• • Our people
• • Our services
• • Our work
• • Contact us/social media
• (Maximum 3 pages)
• domain name, address, our services etc
• Blend colours with logo design colours
Nice to have
• Given the migration to mobile devices, we think that having a site which can be scrolled from top to bottom would be preferable
• Possibly a lite version in areas where bandwidth is poor?
Should not have
• Anything that takes a long time to download

```html
<!DOCTYPE html>
<html lang="en">
<head>
<meta charset="utf-8">
<title>Learning Horizon Collective</title>
<link rel="stylesheet" href="https://fonts.googleapis.com/css2?family=Roboto+Condensed:wght@400;700&family=Roboto:wght@400;500;700&display=swap">
<style>
:root{
  --navy:#26336a;
  --navy-deep:#1b2550;
  --navy-band:#3a4fa3;
  --teal:#3aa8bb;
  --ink:#2a2a2a;
  --muted:#6d6d6d;
  --line:#e4e7ec;
  --soft:#f6f7f9;
  --white:#ffffff;
}
*{box-sizing:border-box;margin:0;padding:0}
html,body{width:1200px;height:3130px;overflow:hidden;background:var(--white)}
body{font-family:"Roboto",Arial,sans-serif;color:var(--ink);font-size:13px;position:relative}
h2,h3,h4{font-weight:400}
.wrap{width:730px;margin:0 auto;position:relative}
.dots{display:flex;gap:6px;justify-content:center;margin-top:10px}
.dots i{width:4px;height:4px;border-radius:50%;background:var(--teal);display:block}
.sq{width:22px;height:22px;display:inline-flex;align-items:center;justify-content:center}
.sq::after{content:"";width:6px;height:6px;border-radius:50%;background:currentColor;opacity:.8}
.btn{font-size:9px;padding:0 20px;height:30px;line-height:30px;text-transform:uppercase;color:var(--white);display:inline-block;white-space:nowrap}

/* top bar */
.topbar{height:25px;background:var(--navy-deep);color:#cfd5ea;font-size:10px;white-space:nowrap}
.topbar .wrap{display:flex;align-items:center;height:25px;gap:18px}
.topbar .right{margin-left:auto;display:flex;align-items:center;gap:14px}
.topbar .sq{color:#aab3d3;width:20px;height:25px;border-left:1px solid #2f3a6a}

/* header */
.header{height:64px;border-bottom:1px solid var(--line)}
.header .wrap{display:flex;align-items:center;height:63px}
.brand{display:flex;align-items:center;gap:10px;white-space:nowrap}
.brand-mark{width:16px;height:16px;background:var(--navy)}
.brand-name{font-family:"Roboto Condensed","Arial Narrow",sans-serif;font-weight:700;color:var(--navy);font-size:20px;letter-spacing:.3px}
.nav{margin-left:auto;display:flex;font-size:10px;white-space:nowrap}
.nav a{padding:0 19px;border-left:1px solid var(--line);text-decoration:none;color:var(--teal)}
.nav a:first-child{border:0;color:var(--ink)}
.nav a:last-child{padding-right:0}

/* hero */
.hero{height:450px;position:relative;background:linear-gradient(100deg,#3b4661 0%,#4a5570 45%,#394257 100%)}
.hero-photo{position:absolute;left:180px;top:0;width:330px;height:450px;background:radial-gradient(ellipse at 50% 45%,#a98670 0%,#6e5648 45%,rgba(70,76,98,0) 75%)}
.hero-text{position:absolute;left:500px;top:124px;width:480px;text-align:center;color:var(--white);white-space:nowrap;font-family:"Roboto Condensed","Arial Narrow",sans-serif}
.hero-text .l1{font-size:26px}
.hero-text .l2{font-size:25px;font-weight:700;margin-top:4px}
.hero-text .l3{font-size:26px;margin-top:4px}
.hero-btns{display:flex;gap:16px;justify-content:center;margin-top:22px}
.btn-fill{background:var(--navy-band)}
.btn-line{border:1px solid #d6d9e2;line-height:28px}
.hero-pager{position:absolute;left:0;right:0;bottom:30px;display:flex;gap:6px;justify-content:center}
.hero-pager i{width:10px;height:3px;background:#7fc6d3;display:block}

/* story */
.story{height:318px;text-align:center;padding-top:46px}
.sec-title{font-family:"Roboto Condensed","Arial Narrow",sans-serif;font-size:22px;font-weight:400;color:var(--ink)}
.story p{font-size:10px;color:var(--muted);line-height:1.8;margin-top:28px}
.story .countries{margin-top:18px;color:var(--ink)}
.joinband{margin-top:24px;height:65px;background:var(--navy);display:flex;align-items:center;padding:0 20px;color:var(--white);text-align:left}
.joinband .ic{width:32px;height:32px;border-radius:50%;background:#3d4a86;margin-right:16px;display:flex;align-items:center;justify-content:center;flex-shrink:0}
.joinband .txt{font-family:"Roboto Condensed","Arial Narrow",sans-serif;font-size:20px;white-space:nowrap}
.joinband .btn{margin-left:auto;background:var(--teal);padding:0 22px}

/* people */
.people{height:605px;background:linear-gradient(90deg,#f3f4f6,#eceef1 50%,#f3f4f6);text-align:center;padding-top:46px}
.people .intro{font-size:10px;color:var(--muted);line-height:1.8;margin-top:14px}
.cards{display:flex;gap:19px;margin-top:38px}
.card{width:231px}
.card .photo{height:250px}
.card h3{font-family:"Roboto Condensed","Arial Narrow",sans-serif;font-size:18px;margin-top:26px}
.card p{font-size:9px;color:var(--muted);line-height:1.6;margin-top:12px;padding:0 12px}
.card .social{display:inline-flex;margin-top:12px;background:#3b3f48}
.card .social .sq{color:#c9cdd6;border-right:1px solid #555}
.card .social .on{background:var(--teal);color:#fff}

/* services */
.services{height:194px;text-align:center;padding-top:40px;border-bottom:1px solid var(--line)}
.services p{font-size:10px;color:var(--muted);line-height:1.8;margin:28px auto 0;width:340px}

/* provide */
.provide{height:578px;background:var(--soft);padding-top:40px;text-align:center}
.grid{display:grid;grid-template-columns:370px 360px;row-gap:38px;margin:40px 0 0 12px;text-align:left}
.item{display:flex;align-items:center;gap:14px;white-space:nowrap}
.ring{width:80px;height:80px;border-radius:50%;border:1px solid #d9dee6;background:var(--white);display:flex;align-items:center;justify-content:center;flex-shrink:0}
.ring.active{background:var(--navy-band);border:6px solid #c9d0ea}
.item .label{font-family:"Roboto Condensed","Arial Narrow",sans-serif;font-size:15px}
.item .more{font-size:9px;color:var(--teal);margin-left:2px}
.provide .bar{display:flex;gap:5px;justify-content:center;margin-top:50px}
.provide .bar i{width:16px;height:3px;background:var(--teal);display:block}
.provide .bar i:first-child{background:var(--navy)}
.provide .note{font-size:10px;color:var(--muted);line-height:1.8;margin:30px auto 0;width:340px}

/* testimonial */
.quote{height:192px;border-top:1px solid var(--line)}
.quote .wrap{display:flex;align-items:center;height:192px;gap:28px}
.arrow{color:var(--navy-band);flex-shrink:0}
.quote .avatar{width:104px;height:104px;border-radius:50%;background:radial-gradient(circle,#a57e66,#5a4a40);border:4px solid #e4e6ea;flex-shrink:0;margin-left:20px}
.quote blockquote{font-size:10px;color:var(--muted);line-height:1.8;width:520px}
.quote cite{display:block;font-style:italic;color:var(--navy-band);font-size:10px;margin-top:8px}

/* work */
.work{height:299px;background:linear-gradient(90deg,#3a4ea0,#3d53a6);color:var(--white)}
.work .wrap{display:flex;padding-top:40px}
.work .copy{width:490px}
.work h2{font-family:"Roboto Condensed","Arial Narrow",sans-serif;font-size:22px}
.work p{font-size:10px;line-height:1.75;margin-top:16px;color:#e6e9f5}
.work .photo{width:230px;height:180px;margin-left:auto;margin-top:18px;border:2px solid #fff}

/* newsletter */
.news{height:94px}
.news .wrap{display:flex;align-items:center;height:94px}
.news h2{font-family:"Roboto Condensed","Arial Narrow",sans-serif;font-size:31px;white-space:nowrap}
.news .input{width:262px;height:30px;border:1px solid #cfd4dc;margin-left:auto;font-size:9px;color:#999;padding:0 10px;line-height:28px}
.news .btn{background:var(--teal);margin-left:20px;width:104px;text-align:center}

/* footer */
.footer{height:287px;background:var(--navy-deep);color:#c7cde4}
.footer .wrap{display:flex;padding-top:44px}
.fcol{width:188px;font-size:9px;line-height:1.6;padding-right:16px}
.fcol:last-child{padding-right:0;width:166px}
.fcol h4{font-family:"Roboto Condensed","Arial Narrow",sans-serif;color:var(--white);font-size:14px;margin-bottom:20px;height:14px}
.fbrand{display:flex;align-items:center;gap:8px;margin-bottom:22px}
.fbrand .brand-mark{background:#fff}
.fbrand .brand-name{color:#fff}
.fcol b{color:#fff;font-weight:500}
.newsitem{display:flex;gap:12px;margin-bottom:18px}
.newsitem .thumb{width:44px;height:42px;flex-shrink:0}
.meta{color:#8fb8d6;font-size:9px;margin-top:4px}
.tweet{display:flex;gap:10px;margin-bottom:16px}
.tweet .mk{width:8px;height:8px;border-radius:50%;background:var(--teal);margin-top:3px;flex-shrink:0}
.tweet .meta{color:var(--teal)}
.fin{height:28px;border:1px solid #59628a;font-size:9px;padding:0 10px;line-height:26px;color:#aab}
.fbtn{height:28px;background:var(--teal);color:#fff;text-align:center;font-size:9px;line-height:28px;margin-top:10px}

.bottombar{height:25px;background:var(--teal);color:#fff;font-size:9px;white-space:nowrap}
.bottombar .wrap{display:flex;align-items:center;height:25px}
.bottombar .social{margin-left:auto;display:flex}
.bottombar .sq{height:25px;border-left:1px solid #5fbccb;color:#e4f5f8}
</style>
</head>
<body>

<div class="topbar">
  <div class="wrap">
    <span>Have any question?</span><span>+971 4 555 0182</span><span>hello@learnhorizonco.com</span>
    <div class="right"><span>Login / Register</span>
      <span style="display:flex"><span class="sq"></span><span class="sq"></span><span class="sq"></span><span class="sq"></span><span class="sq"></span><span class="sq"></span></span>
    </div>
  </div>
</div>

<header class="header">
  <div class="wrap">
    <div class="brand"><span class="brand-mark"></span><span class="brand-name">LHC Learning Horizon</span></div>
    <nav class="nav"><a>Home</a><a>About Us</a><a>Our People</a><a>Our Services</a><a>Our Work</a><a>Contact Us</a></nav>
  </div>
</header>

<section class="hero">
  <div class="hero-photo" role="img" aria-label="Smiling woman pointing toward the headline"></div>
  <div class="hero-text">
    <div class="l1">Lorem Ipsum Has Been The Industry's Design</div>
    <div class="l2">Dummy Text Ever Printer</div>
    <div class="l3">Galley Unknown</div>
    <div class="hero-btns"><span class="btn btn-fill">Get Started</span><span class="btn btn-line">Take a Tour</span></div>
  </div>
  <div class="hero-pager"><i></i><i></i><i></i></div>
</section>

<section class="story">
  <div class="wrap">
    <h2 class="sec-title">Our Story</h2>
    <div class="dots"><i></i><i></i><i></i></div>
    <p>The Partners have extensive international educational consultancy experience and have worked extensively improving schools, universities, education systems with<br>delivery in the following countries:</p>
    <p class="countries">United Kingdom, Australia, Germany, United States, Bahrain, U.A.E, Pakistan, India, South Africa, Saudi Arabia, Jordan.</p>
    <div class="joinband">
      <span class="ic"><svg width="16" height="12" viewBox="0 0 16 12"><circle cx="8" cy="4" r="3" fill="#fff"/><path d="M2 12c0-3 3-5 6-5s6 2 6 5z" fill="#fff"/></svg></span>
      <span class="txt">4000+ People already Joined to our organization, it's the first step</span>
      <span class="btn">Join to us now</span>
    </div>
  </div>
</section>

<section class="people">
  <div class="wrap">
    <h2 class="sec-title">Our People</h2>
    <div class="dots"><i></i><i></i><i></i></div>
    <p class="intro">Lorem Ipsum has been the industry's standard dummy text ever since the 1500s,<br>when an unknown printer took a galley.</p>
    <div class="cards">
      <div class="card">
        <div class="photo" role="img" aria-label="Portrait of Partner A in a classroom" style="background:linear-gradient(135deg,#d9d3c6,#b39a7c 60%,#e8e4dc)"></div>
        <h3>Partner A</h3>
        <p>It has survived not only five centuries, but also the leap into electronic typesetting unchanged.</p>
        <div class="social"><span class="sq"></span><span class="sq"></span><span class="sq"></span><span class="sq"></span></div>
      </div>
      <div class="card">
        <div class="photo" role="img" aria-label="Portrait of Partner B holding books" style="background:linear-gradient(135deg,#c7cbd1,#7d8794 55%,#d6d9de)"></div>
        <h3>Partner B</h3>
        <p>It has survived not only five centuries, but also the leap into electronic typesetting unchanged.</p>
        <div class="social"><span class="sq"></span><span class="sq on"></span><span class="sq"></span><span class="sq"></span></div>
      </div>
      <div class="card">
        <div class="photo" role="img" aria-label="Portrait of Partner C holding folders" style="background:linear-gradient(135deg,#d8c7b4,#9c6c58 55%,#e0a070)"></div>
        <h3>Partner C</h3>
        <p>It has survived not only five centuries, but also the leap into electronic typesetting unchanged.</p>
        <div class="social"><span class="sq"></span><span class="sq"></span><span class="sq"></span><span class="sq"></span></div>
      </div>
    </div>
  </div>
</section>

<section class="services">
  <div class="wrap">
    <h2 class="sec-title">Our Services</h2>
    <div class="dots"><i></i><i></i><i></i></div>
    <p>Learning Horizon Collective design, deliver and support Government education systems, public and private universities, groups of private schools, individual schools.</p>
  </div>
</section>

<section class="provide">
  <div class="wrap">
    <h2 class="sec-title">What We Provide?</h2>
    <div class="dots"><i></i><i></i><i></i></div>
    <div class="grid">
      <div class="item"><span class="ring"><svg width="24" height="24" viewBox="0 0 24 24" fill="var(--teal)"><path d="M6 3h12v5a6 6 0 0 1-12 0z"/><rect x="10" y="14" width="4" height="4"/><rect x="7" y="19" width="10" height="2"/></svg></span><span class="label">Support in developing strategy</span><span class="more">More ..</span></div>
      <div class="item"><span class="ring"><svg width="26" height="22" viewBox="0 0 26 22" fill="var(--teal)"><path d="M13 2 1 8l12 6 12-6z"/><path d="M6 11v5c0 2 3 4 7 4s7-2 7-4v-5l-7 3.5z"/></svg></span><span class="label">Teacher training design and delivery</span><span class="more">More ..</span></div>
      <div class="item"><span class="ring active"><svg width="24" height="22" viewBox="0 0 24 22" fill="#fff"><rect x="2" y="6" width="20" height="14" rx="2"/><rect x="8" y="2" width="8" height="5" fill="none" stroke="#fff" stroke-width="2"/></svg></span><span class="label">School improvement planning</span><span class="more">More ..</span></div>
      <div class="item"><span class="ring"><svg width="24" height="26" viewBox="0 0 24 26" fill="var(--teal)"><rect x="11" y="2" width="2" height="22"/><path d="M4 5h14l3 3-3 3H4z"/><path d="M20 13H7l-3 3 3 3h13z"/></svg></span><span class="label">Curriculum</span><span class="more">More ..</span></div>
      <div class="item"><span class="ring"><svg width="26" height="22" viewBox="0 0 26 22" fill="var(--teal)"><rect x="2" y="6" width="9" height="14" rx="3"/><rect x="15" y="6" width="9" height="14" rx="3"/><rect x="9" y="8" width="8" height="5"/><rect x="4" y="2" width="5" height="5"/><rect x="17" y="2" width="5" height="5"/></svg></span><span class="label">Education reform</span><span class="more">More ..</span></div>
      <div class="item"><span class="ring"><svg width="24" height="24" viewBox="0 0 24 24" fill="var(--teal)"><rect x="10" y="2" width="4" height="10"/><path d="M5 10h14l-7 7z"/><path d="M2 16h4v4h12v-4h4v6H2z"/></svg></span><span class="label">Assessment</span><span class="more">More ..</span></div>
    </div>
    <div class="bar"><i></i><i></i><i></i></div>
    <p class="note">All support is contextualised and delivered with the client and at the highest standards possible.</p>
  </div>
</section>

<section class="quote">
  <div class="wrap">
    <svg class="arrow" width="8" height="12" viewBox="0 0 8 12"><path d="M7 1 2 6l5 5" stroke="currentColor" stroke-width="2" fill="none"/></svg>
    <div class="avatar" role="img" aria-label="Round portrait of the quoted client"></div>
    <blockquote>&ldquo; Lorem Ipsum has been the industry's standard dummy text ever since the 1500s, when an unknown printer took a galley of type and scrambled it to make a type specimen book. Lorem Ipsum has been the industry's standard dummy text ever since the 1500s.<cite>&ndash; Dana Morrell</cite></blockquote>
    <svg class="arrow" width="8" height="12" viewBox="0 0 8 12" style="margin-left:auto"><path d="m1 1 5 5-5 5" stroke="currentColor" stroke-width="2" fill="none"/></svg>
  </div>
</section>

<section class="work">
  <div class="wrap">
    <div class="copy">
      <h2>Our work</h2>
      <p>The Partners have extensive experience in large-scale education reform across the K-12 and higher education sectors. These experiences have included work within advanced and emerging economy countries, as well systems with more than 50,000 schools.</p>
      <p>Impact is a core pillar of the education reform contributions from both partners, from improving student, teacher and school performance, through to improving university reform in short periods of time.</p>
      <p>LHC have access to a range of high calibre and skilled consultants who are matched with the needs of the engagement and required scope of work.</p>
    </div>
    <div class="photo" role="img" aria-label="Teacher helping students at classroom desks" style="background:linear-gradient(135deg,#c9b8a4,#8a9bb0 50%,#d8cfc2)"></div>
  </div>
</section>

<section class="news">
  <div class="wrap">
    <h2>Subscribe to our Newsletter</h2>
    <div class="input">Email</div>
    <span class="btn">Subscribe</span>
  </div>
</section>

<footer class="footer">
  <div class="wrap">
    <div class="fcol">
      <div class="fbrand"><span class="brand-mark"></span><span class="brand-name">LHC</span></div>
      <p><b>Operating Name:</b> Learning Horizon Collective FZE</p>
      <p style="margin-top:12px"><b>Address:</b> Suite 14, Palmview Tower, Harbor Free Zone, Dubai, U.A.E</p>
    </div>
    <div class="fcol">
      <h4>Latest News</h4>
      <div class="newsitem"><span class="thumb" role="img" aria-label="News thumbnail" style="background:linear-gradient(135deg,#b9a690,#5d7a4e)"></span><div>when an unknown printer took a book<div class="meta">April 1, 2016 &nbsp; 12</div></div></div>
      <div class="newsitem"><span class="thumb" role="img" aria-label="News thumbnail" style="background:linear-gradient(135deg,#c4ad94,#4f6e49)"></span><div>when an unknown printer took a book<div class="meta">April 1, 2016 &nbsp; 12</div></div></div>
    </div>
    <div class="fcol">
      <h4>Our Twitter</h4>
      <div class="tweet"><span class="mk"></span><div>when an unknown printer took a galley of type<br><b>https://lhc.link/upd8</b><div class="meta">12 Days ago</div></div></div>
      <div class="tweet"><span class="mk"></span><div>when an unknown printer took a galley of type<div class="meta">29 Days ago</div></div></div>
    </div>
    <div class="fcol">
      <h4>Subscribe</h4>
      <div class="fin">Email</div>
      <div class="fbtn">SUBSCRIBE</div>
      <p style="margin-top:10px">Get the latest updates via email. Any time you may unsubscribe.</p>
    </div>
  </div>
</footer>

<div class="bottombar">
  <div class="wrap">
    <span>Copyright Learning Horizon Collective &copy; 2017. All rights reserved.</span>
    <div class="social"><span class="sq"></span><span class="sq"></span><span class="sq"></span><span class="sq"></span><span class="sq"></span><span class="sq"></span></div>
  </div>
</div>

</body>
</html>
```